Property Management Services Proposal - Powerpoint template

We need a proposal template for our multifamily property management services. We have a simple/generic handout that we use (uploaded here) but we need something for an actual proposal/client presentation standpoint. A powerpoint file that includes company/team overview, some placeholders for the specific client we would be proposing too, etc. Website is www.kellovanpropertygroup.com

Target Market(s)

Residential/Multifamily Property Owners and Investors

Industry/Entity Type

Real Estate

Font styles to use
Sans Serif

Colors
0355a3
f78f20
9d9d9d
ffffff

Requirements
Must have
• Logo, color scheme (orange, navy, gray) - clean look but not overly simple. Placeholders for specific projects, case studies, timelines, photos, graphs, etc.

```html
<!DOCTYPE html>
<html lang="en">
<head>
<meta charset="utf-8">
<title>KPG Management Services Overview</title>
<link href="https://fonts.googleapis.com/css2?family=Tinos:wght@400;700&family=Open+Sans:wght@400;600;700&display=swap" rel="stylesheet">
<style>
:root{
  --navy:#0355a3;
  --orange:#f78f20;
  --gray:#9d9d9d;
  --white:#ffffff;
  --ink:#3a3a3a;
  --paper:#f1f1f1;
  --night:#1d2a48;
}
*{box-sizing:border-box;margin:0;padding:0}
html,body{width:1200px;height:768px;overflow:hidden;background:var(--white)}
body{position:relative;font-family:"Tinos",serif}
.slide{position:absolute;width:390px;height:244px;overflow:hidden;box-shadow:1px 2px 4px rgba(0,0,0,.35)}
.c1{left:5px}.c2{left:405px}.c3{left:805px}
.r1{top:5px}.r2{top:262px}.r3{top:519px}
.abs{position:absolute}
.photo{position:absolute;inset:0}
.rule{position:absolute;left:10px;top:6px;width:26px;height:2px;background:var(--white)}
/* footer band */
.band{position:absolute;left:0;bottom:0;width:390px;height:62px}
.band.orange{background:var(--orange)}
.band.navy{background:var(--navy)}
.band-icon{position:absolute;left:9px;top:15px;width:30px;height:30px;border-radius:50%;background:var(--white);display:flex;align-items:center;justify-content:center}
.band-title{position:absolute;left:46px;top:11px;color:var(--white);font-weight:700;font-size:13px;line-height:15px}
.band-divider{position:absolute;left:137px;top:10px;width:1.5px;height:40px;background:var(--white)}
.band-text{position:absolute;left:146px;top:18px;width:180px;color:var(--white);font-size:7.5px;line-height:9.5px}
.band-corner{position:absolute;right:0;bottom:0}
.corner-name{position:absolute;right:9px;bottom:38px;font-size:11px;color:var(--orange)}
.pageno{position:absolute;right:6px;bottom:3px;font-size:4px;color:var(--ink)}
/* slide 1 */
.cover{background:var(--paper)}
.faint{position:absolute;font-size:8px;color:#d2d2d2}
.cover-name{position:absolute;left:0;width:390px;top:52px;text-align:center;font-size:48px;color:var(--orange);letter-spacing:1px}
.cover-mark{position:absolute;left:187px;top:40px;width:14px;height:14px;background:var(--gray)}
.cover-tag{position:absolute;left:0;width:390px;text-align:center;color:#555;font-size:8px}
.cover-title{position:absolute;left:0;width:390px;top:187px;text-align:center;color:var(--orange);font-size:15px;font-weight:700}
.cover-sub{position:absolute;left:0;width:390px;top:214px;text-align:center;color:#777;font-size:8px}
/* slide 2 */
.mission-title{position:absolute;left:18px;top:10px;color:var(--white);font-size:12px;font-weight:700;line-height:14px}
.mission-lead{position:absolute;right:16px;top:13px;width:230px;text-align:right;color:var(--orange);font-family:"Open Sans",sans-serif;font-weight:600;font-size:7.5px;line-height:10px}
.mission-body{position:absolute;left:15px;top:181px;width:320px;color:var(--white);font-family:"Open Sans",sans-serif;font-weight:600;font-size:7.5px;line-height:10.5px}
/* slide 3 */
.pillar{position:absolute;top:50px;width:113px;height:126px;background:var(--white);border:1.5px solid #f1c28c;border-radius:6px;padding:5px 5px;text-align:center}
.pillar h3{color:var(--navy);font-size:9px;margin-bottom:4px}
.pillar p{font-size:4.6px;line-height:6px;color:#444}
.pillar-icon{position:absolute;top:16px;width:28px;height:28px;border-radius:50%;background:var(--white);border:2px solid var(--orange)}
/* slide 4 */
.service-icon{position:absolute;width:30px;height:30px;border-radius:50%;background:var(--white);border:2px solid #f9c48a;display:flex;align-items:center;justify-content:center}
.service-label{position:absolute;width:88px;height:26px;background:rgba(60,60,60,.82);color:var(--white);font-size:6.5px;font-weight:700;text-align:center;display:flex;align-items:center;justify-content:center;line-height:8px}
/* slide 5 */
.prop-name{position:absolute;top:10px;width:72px;text-align:center;color:var(--white);font-weight:700;font-size:8px;line-height:10px}
.prop-badge{position:absolute;top:35px;width:64px;height:36px;border-radius:5px;background:var(--night);border:1px solid #8a96b8}
.prop-card{position:absolute;top:85px;width:64px;height:78px;background:var(--white);border:1.5px solid #f1c28c;border-radius:5px;padding:5px 4px}
.prop-card h4{color:var(--orange);font-size:5.5px;margin-bottom:3px}
.prop-card li{font-size:5px;line-height:7px;color:#555;margin-left:7px}
.prop-card li::marker{color:var(--orange)}
/* slide 6 */
.portrait{position:absolute;top:33px;width:64px;height:38px;border-radius:4px;background:linear-gradient(#bfbfbf,#7c7c7c)}
.bio{position:absolute;top:78px;width:64px;height:57px;background:var(--white);border-radius:4px;text-align:center;padding:6px 3px}
.bio h4{color:var(--navy);font-size:7px;margin-bottom:3px}
.bio p{font-size:5.5px;line-height:7px;color:#666}
/* slide 7 */
.thanks{position:absolute;left:18px;top:28px;color:var(--white);font-size:18px;font-weight:700;line-height:23px}
.contact{position:absolute;left:147px;color:var(--white);font-size:6.5px;display:flex;align-items:center;gap:6px}
.contact-dot{width:10px;height:10px;border-radius:50%;background:var(--white);display:flex;align-items:center;justify-content:center}
</style>
</head>
<body>

<!-- Slide 1: cover -->
<section class="slide cover c1 r1">
  <span class="faint" style="left:36px;top:27px">We are</span>
  <span class="faint" style="left:242px;top:17px">We are</span>
  <span class="faint" style="left:340px;top:30px">We are</span>
  <span class="faint" style="left:98px;top:63px">We are</span>
  <span class="faint" style="left:310px;top:82px">We are</span>
  <span class="faint" style="left:24px;top:110px">We are</span>
  <span class="faint" style="left:52px;top:148px">We are</span>
  <span class="faint" style="left:340px;top:136px">We are</span>
  <div class="cover-mark"></div>
  <div class="cover-name">KPG</div>
  <div class="cover-tag" style="top:121px">INVESTMENT | MANAGEMENT</div>
  <div class="cover-tag" style="top:138px">(RE)DEVELOPMENT</div>
  <div class="cover-title">MANAGEMENT SERVICES OVERVIEW</div>
  <div class="cover-sub">Finding Opportunity, Creating Value</div>
</section>

<!-- Slide 2: mission -->
<section class="slide c2 r1">
  <div class="photo" role="img" aria-label="Soaring bird against a bright grey sky" style="background:radial-gradient(circle at 78% 30%,#f4f4f4 0,#c9c9c9 35%,#8f8f8f 100%)"></div>
  <svg class="abs" style="left:0;top:0" width="390" height="244" viewBox="0 0 390 244">
    <polygon points="0,0 120,0 0,155" fill="var(--orange)"/>
    <polygon points="0,155 120,0 128,0 0,168" fill="#f7b36a" opacity=".6"/>
    <polygon points="330,244 390,190 390,244" fill="#e6e6e6"/>
  </svg>
  <div class="mission-title">Our<br>Mission</div>
  <div class="mission-lead">KPG specializes in the acquisition and management of multi-family apartment communities.</div>
  <div class="mission-body">KPG utilizes the knowledge and strengths of its employees and local market expertise to provide an array of real estate services to achieve maximum benefit for residents, owners and investors.</div>
  <span class="pageno">2</span>
</section>

<!-- Slide 3: our company -->
<section class="slide c3 r1">
  <div class="photo" role="img" aria-label="Brick apartment building with a porch" style="background:linear-gradient(160deg,#8a8580,#5e5650 60%,#6f5a45)"></div>
  <div class="rule" style="background:var(--navy)"></div>
  <div class="pillar-icon" style="left:55px"></div>
  <div class="pillar-icon" style="left:178px"></div>
  <div class="pillar-icon" style="left:300px"></div>
  <div class="pillar" style="left:13px">
    <h3>Investment</h3>
    <p>Our thorough due diligence plan helps us find value-creation opportunities. Through careful risk reviews and creative debt structures, we deliver strong, steady returns. We source capital directly, without middlemen, keeping investor reports clear, open and on time.</p>
  </div>
  <div class="pillar" style="left:137px">
    <h3>Management</h3>
    <p>We work closely with owners through the full life of each asset, treating every property as our own. Together we build long-term revenue plans, sharp marketing and leasing tactics, and preventive maintenance. Our flat structure means an owner is never far from the leadership team.</p>
  </div>
  <div class="pillar" style="left:261px">
    <h3>(RE) Development</h3>
    <p>As a lean, nimble firm, we move quickly to reach owner goals. By reviewing market conditions and working with trusted contractors, we deliver efficient renovations that extend asset life and raise the owner's ROI.</p>
  </div>
  <div class="band orange">
    <div class="band-icon"><svg width="16" height="14" viewBox="0 0 16 14"><path d="M8 0 L16 7 H13 V14 H3 V7 H0 Z" fill="var(--gray)"/></svg></div>
    <div class="band-title">Our<br>Company</div>
    <div class="band-divider"></div>
    <div class="band-text" style="top:27px">A Seamless Asset Management Experience</div>
  </div>
  <svg class="band-corner" width="70" height="70" viewBox="0 0 70 70"><polygon points="20,8 70,8 70,70 60,70" fill="#f5e4cf"/><polygon points="45,70 70,40 70,70" fill="#fbf1e5"/></svg>
  <span class="corner-name">KPG</span>
  <span class="pageno">3</span>
</section>

<!-- Slide 4: management services -->
<section class="slide c1 r2">
  <div class="photo" role="img" aria-label="Brick house framed by trees" style="background:linear-gradient(160deg,#6b6e68,#4a4d48 50%,#8a8a86)"></div>
  <div class="rule"></div>
  <div class="service-icon" style="left:65px;top:22px"><svg width="14" height="14"><rect x="2" y="4" width="10" height="10" fill="var(--orange)"/></svg></div>
  <div class="service-icon" style="left:181px;top:22px"><svg width="14" height="14"><rect x="1" y="2" width="12" height="8" fill="none" stroke="var(--orange)" stroke-width="1.5"/><rect x="5" y="10" width="4" height="3" fill="var(--orange)"/></svg></div>
  <div class="service-icon" style="left:292px;top:22px"><svg width="16" height="12"><rect x="0" y="2" width="10" height="7" fill="var(--orange)"/><rect x="10" y="4" width="5" height="5" fill="var(--orange)"/><circle cx="3" cy="10" r="1.6" fill="var(--orange)"/><circle cx="12" cy="10" r="1.6" fill="var(--orange)"/></svg></div>
  <div class="service-label" style="left:36px;top:58px">24/7/365 Owner account access via our platform</div>
  <div class="service-label" style="left:152px;top:58px">Leading Industry Technology</div>
  <div class="service-label" style="left:263px;top:58px">90% of Work Orders Serviced In-House</div>
  <div class="service-icon" style="left:65px;top:101px"><svg width="14" height="14"><circle cx="7" cy="4" r="3" fill="var(--orange)"/><rect x="3" y="8" width="8" height="5" fill="var(--orange)"/></svg></div>
  <div class="service-icon" style="left:181px;top:101px"><svg width="16" height="16"><circle cx="8" cy="8" r="7" fill="none" stroke="var(--orange)" stroke-width="1.5"/><circle cx="8" cy="8" r="4" fill="none" stroke="var(--orange)" stroke-width="1.5"/><circle cx="8" cy="8" r="1.5" fill="var(--orange)"/></svg></div>
  <div class="service-icon" style="left:292px;top:101px"><svg width="14" height="14"><rect x="1" y="5" width="4" height="9" fill="var(--navy)"/><rect x="5" y="2" width="5" height="12" fill="var(--orange)"/><rect x="10" y="7" width="3" height="7" fill="var(--navy)"/></svg></div>
  <div class="service-label" style="left:36px;top:137px">Resident Screening From Every Angle</div>
  <div class="service-label" style="left:152px;top:137px">Targeted And Effective Marketing</div>
  <div class="service-label" style="left:263px;top:137px">Local Area Expertise and Network</div>
  <div class="band navy">
    <div class="band-icon"><svg width="16" height="16" viewBox="0 0 16 16"><circle cx="8" cy="8" r="5" fill="none" stroke="var(--gray)" stroke-width="3" stroke-dasharray="2.5 1.5"/><circle cx="8" cy="8" r="2" fill="var(--gray)"/></svg></div>
    <div class="band-title">Management<br>Services</div>
    <div class="band-divider"></div>
    <div class="band-text">KPG provides a variety of property management services.</div>
  </div>
  <svg class="band-corner" width="70" height="70" viewBox="0 0 70 70"><polygon points="20,8 70,8 70,70 60,70" fill="#dfe6ef"/><polygon points="45,70 70,40 70,70" fill="#f0f3f7"/></svg>
  <span class="corner-name">KPG</span>
  <span class="pageno">4</span>
</section>

<!-- Slide 5: partial portfolio -->
<section class="slide c2 r2">
  <div class="photo" role="img" aria-label="Apartment buildings on a tree-lined street" style="background:linear-gradient(160deg,#5b5d63,#3c3e44 55%,#77787c)"></div>
  <div class="rule"></div>
  <div class="prop-name" style="left:37px">Birchwood<br>Square</div>
  <div class="prop-name" style="left:117px">Stone Creek<br>Village</div>
  <div class="prop-name" style="left:197px">Maple Ridge<br>Apartments</div>
  <div class="prop-name" style="left:277px">Harbor<br>Green</div>
  <div class="prop-badge" style="left:41px"></div>
  <div class="prop-badge" style="left:121px"></div>
  <div class="prop-badge" style="left:201px"></div>
  <div class="prop-badge" style="left:281px"></div>
  <div class="prop-card" style="left:41px"><h4>Bloomington, IN</h4><ul><li>200 Units</li><li>26 Buildings</li><li>208,660 SQ. FT.</li><li>96% Avg. Occupancy</li></ul></div>
  <div class="prop-card" style="left:121px"><h4>Anderson, IN</h4><ul><li>89 Units</li><li>8 Buildings</li><li>70,064 SQ. FT.</li><li>95% Avg. Occupancy</li></ul></div>
  <div class="prop-card" style="left:201px"><h4>Muncie, IN</h4><ul><li>112 Units</li><li>16 Buildings</li><li>112,000 SQ. FT.</li><li>91% Avg. Occupancy</li></ul></div>
  <div class="prop-card" style="left:281px"><h4>Indianapolis, IN</h4><ul><li>237 Units</li><li>16 Buildings</li><li>251,867 SQ. FT.</li><li>96% Avg. Occupancy</li></ul></div>
  <div class="band orange">
    <div class="band-icon"><svg width="16" height="13" viewBox="0 0 16 13"><rect x="0.5" y="0.5" width="15" height="12" fill="none" stroke="var(--gray)"/><polygon points="2,11 6,5 9,9 11,7 14,11" fill="var(--gray)"/></svg></div>
    <div class="band-title" style="top:6px">Partial<br>Portfolio<br>Summary</div>
    <div class="band-divider"></div>
    <div class="band-text">KPG developed a dynamic and strong portfolio, based on the services quality and the team professionalism.</div>
  </div>
  <svg class="band-corner" width="70" height="70" viewBox="0 0 70 70"><polygon points="20,8 70,8 70,70 60,70" fill="#f5e4cf"/><polygon points="45,70 70,40 70,70" fill="#fbf1e5"/></svg>
  <span class="corner-name">KPG</span>
  <span class="pageno">5</span>
</section>

<!-- Slide 6: executive team -->
<section class="slide c3 r2">
  <div class="photo" role="img" aria-label="Silhouetted group of people at sunset" style="background:linear-gradient(180deg,#6e6e6e,#3e3e3e 55%,#8d8d8d)"></div>
  <div class="rule"></div>
  <div class="portrait" role="img" aria-label="Portrait of Owen Castell" style="left:43px"></div>
  <div class="portrait" role="img" aria-label="Portrait of Lena Farrow" style="left:121px"></div>
  <div class="portrait" role="img" aria-label="Portrait of Marcus Dale" style="left:205px"></div>
  <div class="portrait" role="img" aria-label="Portrait of Tessa Ruiz" style="left:285px"></div>
  <div class="bio" style="left:43px"><h4>Owen Castell</h4><p>CEO and Founder</p></div>
  <div class="bio" style="left:121px"><h4>Lena Farrow</h4><p>Principal, VP of Acquisitions &amp; Asset Management</p></div>
  <div class="bio" style="left:205px"><h4>Marcus Dale</h4><p>Director of Maintenance</p></div>
  <div class="bio" style="left:285px"><h4>Tessa Ruiz</h4><p>Director of Financial &amp; Operations</p></div>
  <div class="band navy">
    <div class="band-icon"><svg width="16" height="16" viewBox="0 0 16 16"><rect x="1" y="6" width="8" height="4" rx="2" transform="rotate(-45 5 8)" fill="none" stroke="var(--gray)" stroke-width="1.6"/><rect x="7" y="6" width="8" height="4" rx="2" transform="rotate(-45 11 8)" fill="none" stroke="var(--gray)" stroke-width="1.6"/></svg></div>
    <div class="band-title">Executive<br>Team</div>
    <div class="band-divider"></div>
    <div class="band-text" style="width:190px">Our team will maximize your property value and will help you maximize your benefits.</div>
  </div>
  <svg class="band-corner" width="70" height="70" viewBox="0 0 70 70"><polygon points="20,8 70,8 70,70 60,70" fill="#dfe6ef"/><polygon points="45,70 70,40 70,70" fill="#f0f3f7"/></svg>
  <span class="corner-name">KPG</span>
  <span class="pageno">6</span>
</section>

<!-- Slide 7: contact -->
<section class="slide c1 r3">
  <div class="photo" role="img" aria-label="Person in a suit holding a smartphone" style="background:linear-gradient(120deg,#3a3a3a,#6d6d6d 45%,#d6d6d6 80%,#eeeeee)"></div>
  <div class="rule"></div>
  <div class="thanks">Thank YOU for<br>your TIME !</div>
  <div class="band orange">
    <div class="band-icon"><svg width="16" height="14" viewBox="0 0 16 14"><ellipse cx="8" cy="6" rx="7" ry="5" fill="none" stroke="var(--gray)" stroke-width="1.6"/><polygon points="3,10 2,14 7,11" fill="var(--gray)"/></svg></div>
    <div class="band-title">Contact<br>Details</div>
    <div class="band-divider"></div>
    <div class="contact" style="top:9px"><span class="contact-dot"><svg width="6" height="6"><path d="M1 0 L2.5 0 L3 2 L2 2.7 Q2.8 4 4 4.6 L4.6 3.6 L6 4 L6 5.5 Q3 6 0.5 3 Q0 1 1 0Z" fill="var(--orange)"/></svg></span>317.555.0148</div>
    <div class="contact" style="top:26px"><span class="contact-dot"><svg width="6" height="6"><circle cx="3" cy="3" r="2.4" fill="none" stroke="var(--orange)"/></svg></span>www.kellovanpropertygroup.com</div>
    <div class="contact" style="top:43px"><span class="contact-dot"><svg width="6" height="7"><path d="M3 7 L0.6 3.4 A2.6 2.6 0 1 1 5.4 3.4Z" fill="var(--orange)"/></svg></span>418 North Meridian Street, Indianapolis, IN 46204</div>
  </div>
  <svg class="band-corner" width="70" height="70" viewBox="0 0 70 70"><polygon points="20,8 70,8 70,70 60,70" fill="#f5e4cf"/><polygon points="45,70 70,40 70,70" fill="#fbf1e5"/></svg>
  <span class="corner-name">KPG</span>
  <span class="pageno">7</span>
</section>

</body>
</html>
```